KLR Lending Website

Need a web site designed for a Professional Mortgage company along the lines of the draft site www.klrlending-demo.com.au

The main purpose of the site is to provide a professional image of the company and capture email address's and send out simple messages. ie "INTEREST RATE SPECIAL 4.5% FOR THE MONTH OF JUNE" or whatever...basically short punchy messages to hook people.

The content is important but a lot of that can be provided by links to our lender panel, several of which have been set up.

Most people will want to know current interest rates, and how much they can borrow along with what it will cost. There are various calculators embedded in the lenders sites such as "Repayment Calculators" Borrow Capacity Calculators" Stamp Duty Calculators"

These would be nice to have on site, but if to costly or difficult to start the links can suffice.

The site will need to be updated/amended regularily.

Example "Interest Rate Special" or "Current Special Offer" sections would be required and would need to be easyily editable and in fact would need to be able to switch them off if there is no special running.

Target Market(s)

Target market is a broad spectrum of people from young couple buying first home to older couples investing.

Industry/Entity Type

It Company

Requirements
Must have
• email capture, preferably need to enter email to enter site.

```html
<!DOCTYPE html>
<html lang="en">
<head>
<meta charset="utf-8">
<title>KLR Lending Services</title>
<link rel="stylesheet" href="https://fonts.googleapis.com/css2?family=Open+Sans:wght@400;600;700&family=Roboto+Condensed:wght@400;700&family=Roboto:wght@400;500;700&display=swap">
<style>
:root{
  --ink:#222428;
  --muted:#666a70;
  --heading-grey:#5a5d62;
  --link-blue:#2d62b0;
  --band-blue:#1f5cb8;
  --band-deep:#1747a0;
  --footer-blue:#0c2f8c;
  --footer-deep:#071f6a;
  --footer-text:#a9b8dc;
  --footer-head:#8fa2d0;
  --bar-dark:#1b1b1d;
  --header-dark:#262729;
  --accent-yellow:#f6b21c;
  --white:#ffffff;
}
*{box-sizing:border-box;margin:0;padding:0}
html,body{width:790px;height:1200px;overflow:hidden;background:var(--white)}
body{position:relative;font-family:"Roboto",Arial,sans-serif;color:var(--ink)}
.abs{position:absolute}
a{color:inherit;text-decoration:none}

/* header */
.site-header{left:0;top:0;width:790px;height:49px;background:linear-gradient(#3a3b3e,var(--header-dark))}
.brand{left:106px;top:17px;font:700 12px "Open Sans",sans-serif;color:var(--white)}
.main-nav{right:100px;top:21px;display:flex;gap:23px;font:600 8.5px "Open Sans",sans-serif;color:var(--white)}

/* hero */
.hero{left:0;top:49px;width:790px;height:279px;background:var(--white);overflow:hidden}
.hero-photo{position:absolute;left:292px;top:0;width:498px;height:279px;background:linear-gradient(90deg,rgba(255,255,255,1) 0%,rgba(232,240,250,.6) 12%,transparent 30%),linear-gradient(170deg,#7fb0e8 0%,#c9dcf3 40%,#e9eef3 62%,#6d8f4a 100%)}
.hero-title{position:absolute;left:106px;top:70px;font:700 18px/22px "Open Sans",sans-serif;color:var(--ink)}
.hero-title .rate{color:var(--band-blue)}
.hero-text{position:absolute;left:108px;top:127px;width:228px;font:600 7px/11px "Open Sans",sans-serif;color:var(--muted)}
.btn-learn{position:absolute;left:105px;top:172px;width:100px;height:32px;border-radius:3px;background:linear-gradient(#5db2f0,#2c86d8);color:var(--white);font:600 9.5px/32px "Open Sans",sans-serif;text-align:center}

/* email capture */
.capture{left:0;top:328px;width:790px;height:127px;background:radial-gradient(ellipse at 50% 20%,#2f6ed0,var(--band-deep) 75%)}
.capture-title{left:0;width:790px;top:24px;text-align:center;font:700 17.5px "Open Sans",sans-serif;color:var(--white)}
.capture-field{left:147px;top:56px;width:304px;height:34px;background:#e2e2e2;color:#8a8a8a;font:400 12px/34px "Open Sans",sans-serif;padding-left:14px}
.capture-btn{left:451px;top:56px;width:133px;height:34px;background:var(--accent-yellow);color:#fff8e6;font:600 11.5px/34px "Open Sans",sans-serif;text-align:center}
.capture-btn svg{vertical-align:-1px;margin-right:4px}
.capture-note{left:0;width:790px;top:102px;text-align:center;font:600 7.5px "Open Sans",sans-serif;color:#0d2a66}
.capture-note a{text-decoration:underline}

/* content */
.section-title{font:400 11.5px "Roboto Condensed",sans-serif;letter-spacing:.6px;color:var(--heading-grey);text-transform:uppercase}
.about-photo{left:103px;top:501px;width:183px;height:86px;background:linear-gradient(100deg,#8fc4ea,#f3d8b6 45%,#e26a2e 70%,#9fc2e2)}
.about-title{left:306px;top:511px}
.about-text{left:306px;top:532px;width:385px;font:400 6.2px/9.5px Arial,sans-serif;color:var(--ink)}
.read-more{font:700 6.3px "Roboto",sans-serif;color:var(--link-blue);letter-spacing:.4px}
.about-more{left:306px;top:575px}
.col-title{top:640px}
.col-photo{top:663px;width:183px;height:86px}
.col-text{top:761px;width:185px;font:400 6.3px/9.5px Arial,sans-serif;color:var(--ink)}
.col-more{top:803px}
.p-services{background:linear-gradient(120deg,#8f8a82,#f1f0ec 45%,#d7d5cf)}
.p-calc{background:linear-gradient(120deg,#bfc6cf,#e9ecef 50%,#6b7480)}
.p-offer{background:linear-gradient(180deg,#9ec4e6,#c45a3a 40%,#a86a3c 70%,#5d8a3e)}

/* footer */
.footer{left:0;top:860px;width:790px;height:295px;background:radial-gradient(ellipse at 45% 10%,#1d4fae,var(--footer-blue) 50%,var(--footer-deep))}
.footer-logo{left:103px;top:58px;font:400 21px "Open Sans",sans-serif;color:#0a2a7a;letter-spacing:1px}
.f-head{font:400 10.5px "Roboto Condensed",sans-serif;letter-spacing:.6px;color:var(--footer-head);text-transform:uppercase}
.f-text{font:400 6px/9.5px Arial,sans-serif;color:var(--footer-text)}
.contact-list{list-style:none}
.contact-list li{display:flex;align-items:center;gap:9px;height:15px;font:600 6px Arial,sans-serif;color:var(--footer-text)}
.newsletter{left:533px;top:28px;width:149px;height:101px;background:#2a2a2c}
.newsletter h3{position:absolute;left:27px;top:10px;font:500 6.5px "Roboto",sans-serif;color:var(--white);letter-spacing:.3px}
.newsletter p{position:absolute;left:9px;top:24px;font:400 5.8px Arial,sans-serif;color:#c8c8c8}
.nl-field{position:absolute;left:9px;top:38px;width:131px;height:20px;background:#e6e6e6;font:400 5.5px/20px Arial,sans-serif;color:#777;padding-left:7px}
.nl-btn{position:absolute;left:9px;top:67px;width:131px;height:21px;background:#0b2e8c;color:var(--white);font:700 8px/21px "Roboto",sans-serif;text-align:center;letter-spacing:.6px}
.f-rule{left:103px;top:150px;width:579px;height:1px;background:rgba(140,165,220,.3)}
.f-links{list-style:none}
.f-links li{font:600 5.8px/12px Arial,sans-serif;color:#d5ddf0}
.f-links li::before{content:"";display:inline-block;width:0;height:0;border-left:3px solid #d5ddf0;border-top:2.5px solid transparent;border-bottom:2.5px solid transparent;margin-right:6px}
.social-list{list-style:none}
.social-list li{display:flex;align-items:center;gap:8px;height:19px;font:600 5.8px Arial,sans-serif;color:#d5ddf0}
.social-dot{width:12px;height:12px;border-radius:50%;background:#5b6f97}

/* bottom bar */
.bottom-bar{left:0;top:1155px;width:790px;height:45px;background:var(--bar-dark);font:400 6.5px Arial,sans-serif;color:#cfcfcf}
.copyright{left:104px;top:20px}
.legal-links{right:111px;top:20px;display:flex;gap:7px}
</style>
</head>
<body>

<header class="site-header abs">
  <div class="brand abs">KLR Lending Services</div>
  <nav class="main-nav abs">
    <a href="#">Home</a><a href="#">Services</a><a href="#">Clients</a><a href="#">Partners</a><a href="#">About</a><a href="#">Contact</a>
  </nav>
</header>

<section class="hero abs">
  <div class="hero-photo" role="img" aria-label="White two-storey house with a blue tiled roof under a clear sky"></div>
  <h1 class="hero-title">Special Interest Rate of <span class="rate">4.5%</span><br>for the month of June.</h1>
  <p class="hero-text">KLR Lending offers a complete range of finance solutions tailored to meet individual client needs.</p>
  <a class="btn-learn" href="#">Learn More</a>
</section>

<section class="capture abs">
  <h2 class="capture-title abs">Enter your email and receive exclusive special rates!</h2>
  <div class="capture-field abs">Your Email Address..</div>
  <div class="capture-btn abs"><svg width="10" height="10" viewBox="0 0 10 10"><path d="M1 9l1-3 5-5 2 2-5 5z" fill="#fff8e6"/></svg>Sign up for FREE</div>
  <p class="capture-note abs">Your email will be held in strictest of confidentiality. <a href="#">Privacy Policy</a></p>
</section>

<div class="about-photo abs" role="img" aria-label="Small model house held in an open hand"></div>
<h2 class="section-title about-title abs">About KLR Lending Services</h2>
<p class="about-text abs">KLR Lending Services offers a complete range of Mortgage and Loan products to suit our individual clients needs.<br>Whether your a First Home Buyer, Up-Sizing or Down-Sizing, Refinancing, Investing or simply want a new car or equipment purchase, contact us for a no obligation assessment and get the lastest information on the available products to suit you needs.</p>
<a class="read-more about-more abs" href="#">READ MORE ›</a>

<h2 class="section-title col-title abs" style="left:103px">Our Services</h2>
<div class="col-photo p-services abs" style="left:103px" role="img" aria-label="Loan paperwork and forms on a desk"></div>
<p class="col-text abs" style="left:103px">Lorem ipsum dolor sit amet, consectetur adipisicing elit, sed do eiusmod tempor incididunt ut labore et dolore magna aliqua. Ut enim ad minim veniam, quis nostrud exercitation.</p>
<a class="read-more col-more abs" style="left:103px" href="#">READ MORE ›</a>

<h2 class="section-title col-title abs" style="left:300px">Repayment Calculators</h2>
<div class="col-photo p-calc abs" style="left:300px" role="img" aria-label="Calculator and glasses on financial papers"></div>
<p class="col-text abs" style="left:300px">Lorem ipsum dolor sit amet, consectetur adipisicing elit, sed do eiusmod tempor incididunt ut labore et dolore magna aliqua. Ut enim ad minim veniam, quis nostrud exercitation.</p>
<a class="read-more col-more abs" style="left:300px" href="#">READ MORE ›</a>

<h2 class="section-title col-title abs" style="left:498px">Current Special Offer</h2>
<div class="col-photo p-offer abs" style="left:498px" role="img" aria-label="Timber house with a red roof on a green lawn"></div>
<p class="col-text abs" style="left:498px">Lorem ipsum dolor sit amet, consectetur adipisicing elit, sed do eiusmod tempor incididunt ut labore et dolore magna aliqua. Ut enim ad minim veniam, quis nostrud exercitation.</p>
<a class="read-more col-more abs" style="left:498px" href="#">READ MORE ›</a>

<footer class="footer abs">
  <div class="footer-logo abs">LOGO</div>

  <h3 class="f-head abs" style="left:236px;top:40px">What we do</h3>
  <div class="f-text abs" style="left:236px;top:60px;width:115px">Duis mollis, est non commodo luctus, nisi erat porttitor ligula, eget lacinia odio sem nec elit. Vestibulum id ligula porta felis euismod semper. Integer posuere erat a ante.<br><br>Vestibulum id ligula porta felis euismod semper. Integer posuere erat a ante.</div>

  <h3 class="f-head abs" style="left:383px;top:40px">Contact</h3>
  <div class="f-text abs" style="left:385px;top:60px;width:115px">There are many variations of passages of Lorem Ipsum available, but the majority have suffered alteration.</div>
  <ul class="contact-list abs" style="left:386px;top:96px">
    <li><svg width="7" height="9" viewBox="0 0 7 9"><path d="M3.5 0a3.2 3.2 0 0 0-3.2 3.2C.3 5.6 3.5 9 3.5 9s3.2-3.4 3.2-5.8A3.2 3.2 0 0 0 3.5 0z" fill="#a9b8dc"/><circle cx="3.5" cy="3.2" r="1.1" fill="#0c2f8c"/></svg>Riverton</li>
    <li><svg width="8" height="6" viewBox="0 0 8 6"><rect width="8" height="6" fill="#a9b8dc"/><path d="M0 0l4 3.5L8 0" stroke="#0c2f8c" fill="none" stroke-width=".8"/></svg>info@klrlending-demo.com.au</li>
    <li><svg width="8" height="8" viewBox="0 0 8 8"><path d="M1.6 0l1.6 2-1 1.1a5 5 0 0 0 2.7 2.7l1.1-1L8 6.4 6.9 8C3 7.6.4 5 0 1.1z" fill="#a9b8dc"/></svg>555-0142-7731</li>
  </ul>

  <div class="newsletter abs">
    <svg class="abs" style="left:9px;top:9px" width="12" height="9" viewBox="0 0 12 9"><rect width="12" height="9" fill="#9a9a9a"/><path d="M0 0l6 5 6-5" stroke="#2a2a2c" fill="none"/></svg>
    <h3>SUBSCRIBE TO OUR NEWSLETTER</h3>
    <p>Sign up and get the latest news and updates.</p>
    <div class="nl-field">Enter your email address</div>
    <div class="nl-btn">SUBSCRIBE TODAY</div>
  </div>

  <div class="f-rule abs"></div>

  <h3 class="f-head abs" style="left:102px;top:190px">Site Links</h3>
  <ul class="f-links abs" style="left:104px;top:209px">
    <li>Home</li><li>About</li><li>Services</li><li>Partners</li><li>Contact</li>
  </ul>

  <h3 class="f-head abs" style="left:251px;top:190px">Services</h3>
  <ul class="f-links abs" style="left:252px;top:209px">
    <li>New Home</li><li>First Home Owner Mortgage</li><li>Refinance</li><li>Investmentt</li>
  </ul>
  <ul class="f-links abs" style="left:386px;top:209px">
    <li>Bridging</li><li>Car Loan</li><li>Plant &amp; Equipment</li><li>Insurance</li>
  </ul>

  <h3 class="f-head abs" style="left:533px;top:190px">Social</h3>
  <ul class="social-list abs" style="left:533px;top:207px">
    <li><span class="social-dot"></span>Like us on Friendbook</li>
    <li><span class="social-dot"></span>Follow us on Chirper</li>
    <li><span class="social-dot"></span>Add us in WorkLinks</li>
  </ul>
</footer>

<div class="bottom-bar abs">
  <p class="copyright abs">Copyright 2013 © KLR Lending Services - All Rights Reserved</p>
  <nav class="legal-links abs"><a href="#">Site Map</a><span>•</span><a href="#">Privacy Policy</a><span>•</span><a href="#">Disclaimer</a></nav>
</div>

</body>
</html>
```